We need a tri-fold brochure for our business called: KindleSprout. (KindleSprout Therapy Services)
This is a therapy services business that offers Physiotherapy and Occupational Therapy to children aged 5 to 16 years of age. The focus is on Neuro-developmental therapy and the children have a range of conditions such as Cerebral-Palsy, brain injuries etc... We are looking for designs that focus on children, fun and the word nurture.
Target Market(s)
Primarily parents and people looking for therapy services.
Industry/Entity Type
Business
Font styles to use
Sans Serif

```html
<!DOCTYPE html>
<html lang="en">
<head>
<meta charset="utf-8">
<title>KindleSprout Therapy Services – Tri-fold Brochure</title>
<link rel="stylesheet" href="https://fonts.googleapis.com/css2?family=Open+Sans:wght@300;400;600;700;800&display=swap">
<style>
:root{
  --green:#8cc63f;
  --green-dark:#6fae2a;
  --blue:#3f7fd0;
  --sky:#29a8e0;
  --orange:#f7941d;
  --ink:#444;
  --paper:#fff;
  --bg:#a7a9ac;
}
*{box-sizing:border-box;margin:0;padding:0}
html,body{width:832px;height:1200px;overflow:hidden;background:var(--bg)}
body{font-family:"Open Sans",Arial,sans-serif;color:var(--ink)}
.stage{position:absolute;left:0;top:0;width:955px;height:1378px;transform:scale(.8712,.8708);transform-origin:0 0}
.sheet{position:absolute;left:80px;width:800px;height:620px;background:var(--paper);overflow:hidden}
.sheet--outside{top:47px}
.sheet--inside{top:698px}
.panel{position:absolute;top:0;height:620px;overflow:hidden}
.abs{position:absolute}
.photo{position:absolute}
h2.title{font-weight:700;font-size:24px;line-height:1;letter-spacing:-.2px}
.sub{font-size:12px;font-weight:400}
.copy{font-size:11px;line-height:13.3px}
.justify{text-align:justify}
.center{text-align:center}
.white{color:#fff}
.tag{font-weight:300;font-size:14px;line-height:18px;text-align:center;z-index:3}
.tag .b{color:#2aa3dc}.tag .o{color:var(--orange)}
.brand-name{font-weight:400;font-size:20px;letter-spacing:.2px;color:var(--orange);text-align:center;line-height:1}
.brand-sub{font-size:9px;letter-spacing:4px;text-align:center;line-height:1}
.brand-dot{position:absolute;border-radius:50%}
.contact{font-size:10px;line-height:12px;color:#fff}
.contact span{display:inline-block;width:43px}
.tile{position:absolute;width:75px;height:75px;color:#fff;font-size:9px;line-height:9px;text-align:center}
.tile svg{display:block;margin:5px auto 3px}
.tile.g{background:var(--green)}.tile.s{background:var(--sky)}
.feature{position:absolute;left:24px;width:230px}
.feature .ico{position:absolute;left:0;top:0;width:52px;height:52px;border-radius:50%;background:#fff}
.feature h4{position:absolute;left:65px;top:-3px;font-size:11px;font-weight:600;color:#fff}
.feature p{position:absolute;left:65px;top:12px;width:160px;font-size:9.2px;line-height:12px;color:#fff}
</style>
</head>
<body>
<div class="stage">

  <section class="sheet sheet--outside">

    <div class="panel" style="left:0;width:267px">
      <h2 class="title abs" style="left:28px;top:38px;color:var(--green)">LOREM IPSUM</h2>
      <p class="sub abs" style="left:28px;top:63px">Dolor Set Emet</p>
      <p class="copy justify abs" style="left:28px;top:91px;width:210px">Lorem ipsum dolor sit amet, consectetur adipiscing elit, sed do eiusmod tempor incididunt ut labore et dolore magna aliqua. Ut enim ad minim veniam, quis nostrud exercitation ullamco laboris nisi ut aliquip ex ea commodo consequat.</p>
      <div class="abs" style="left:28px;top:186px;width:210px;height:108px;background:var(--orange);padding:10px 14px">
        <p class="center white" style="font-size:9px;line-height:12px">Lorem ipsum dolor sit amet, consectetur adipiscing elit, sed do eiusmod tempor incididunt ut labore et dolore magna aliqua. Ut enim ad minim veniam, quis nostrud exercitation ullamco laboris nisi ut aliquip ex ea commodo consequat.</p>
      </div>
      <p class="copy center abs" style="left:38px;top:314px;width:190px">Lorem ipsum dolor sit amet, consectetur adipiscing elit, sed do eiusmod tempor incididunt ut labore et dolore magna aliqua.</p>
      <div class="photo" role="img" aria-label="Photo of a toddler playing with a therapist at a small craft table" style="left:0;top:440px;width:267px;height:180px;background:linear-gradient(135deg,#e9d9cf,#c99a86 55%,#6b6f86)"></div>
      <svg class="abs" style="left:0;top:410px" width="267" height="80" viewBox="0 0 267 80">
        <path d="M0 20C90 40 190 46 267 36V0H0Z" fill="#fff"/>
        <path d="M0 20C90 40 190 46 267 36V46C190 60 90 62 0 46Z" fill="var(--green)"/>
        <path d="M0 46C90 62 190 60 267 46V50C190 66 90 68 0 52Z" fill="#fff"/>
      </svg>
      <p class="tag abs" style="left:0;top:391px;width:267px"><span class="b">NEURO-DEVELOPMENTAL</span><br><span class="o">THERAPY</span></p>
    </div>

    <div class="panel" style="left:267px;width:265px;background:var(--blue)">
      <div class="photo" role="img" aria-label="Faint photo of a child in therapy behind the blue panel" style="inset:0;background:radial-gradient(circle at 60% 25%,rgba(255,255,255,.12),transparent 55%),radial-gradient(circle at 30% 65%,rgba(20,60,140,.25),transparent 60%)"></div>
      <h2 class="title abs" style="left:36px;top:159px;color:var(--green)">LOREM IPSUM</h2>
      <p class="sub abs white" style="left:36px;top:184px">Dolor Set Emet</p>
      <p class="copy justify abs white" style="left:36px;top:207px;width:169px">Lorem ipsum dolor sit amet, consectetur adipiscing elit, sed do eiusmod tempor incididunt ut labore et dolore magna aliqua. Ut enim ad minim veniam, quis nostrud exercitation ullamco laboris nisi ut aliquip ex ea commodo consequat.</p>
      <span class="brand-dot" style="left:96px;top:385px;width:38px;height:38px;background:var(--orange)"></span>
      <p class="brand-name abs" style="left:0;top:466px;width:265px">KindleSprout</p>
      <p class="brand-sub abs white" style="left:0;top:488px;width:265px">THERAPY SERVICES</p>
      <div class="contact abs" style="left:37px;top:519px">
        <p><span>Phone</span>123-456-7890</p>
        <p><span>Fax</span>123-456-7890</p>
        <p><span>Email</span>info@kindlesprout-care.com</p>
        <p style="margin-top:17px">address line 1 goes here</p>
        <p>PoBox address 12345</p>
      </div>
    </div>

    <div class="panel" style="left:532px;width:268px">
      <span class="brand-dot" style="left:111px;top:45px;width:46px;height:46px;background:var(--sky)"></span>
      <p class="brand-name abs" style="left:0;top:124px;width:268px">KindleSprout</p>
      <p class="brand-sub abs" style="left:0;top:143px;width:268px;color:#555">THERAPY SERVICES</p>
      <div class="photo" role="img" aria-label="Photo of a smiling girl and her mother building with colourful blocks" style="left:0;top:240px;width:268px;height:380px;background:linear-gradient(160deg,#cfd6d3,#b9a18f 45%,#d04545 75%,#3c7cc4)"></div>
      <svg class="abs" style="left:0;top:190px" width="268" height="92" viewBox="0 0 268 92">
        <path d="M0 0H268V6C180 14 80 40 0 63Z" fill="#fff"/>
        <path d="M0 63C80 40 180 14 268 6V33C180 38 80 58 0 78Z" fill="var(--orange)"/>
        <path d="M0 78C80 58 180 38 268 33V37C180 42 80 62 0 82Z" fill="#fff"/>
      </svg>
      <p class="tag abs" style="left:0;top:162px;width:268px"><span class="b">NEURO-DEVELOPMENTAL</span><br><span class="o">THERAPY</span></p>
    </div>
  </section>

  <section class="sheet sheet--inside">

    <div class="panel" style="left:0;width:268px;background:var(--sky)">
      <div class="photo" role="img" aria-label="Photo of a mother and son stacking wooden blocks on a rug" style="left:0;top:0;width:268px;height:290px;background:linear-gradient(150deg,#efe9df,#c8b49a 50%,#9b8a74)"></div>
      <svg class="abs" style="left:0;top:180px" width="268" height="110" viewBox="0 0 268 110">
        <path d="M0 78C90 70 190 40 268 0V110H0Z" fill="var(--orange)"/>
        <path d="M0 94C90 86 190 56 268 14V110H0Z" fill="var(--sky)"/>
      </svg>
      <h2 class="title abs white" style="left:23px;top:298px">ABOUT COMPANY</h2>
      <p class="sub abs white" style="left:23px;top:323px">Short Summary</p>
      <p class="copy abs white" style="left:23px;top:360px;width:220px">Ut enim ad minim veniam, quis nostrud exercitation ullamco laboris nisi ut aliquip ex ea commodo consequat.</p>
      <p class="copy abs white" style="left:23px;top:413px;font-weight:600">Lorem Ipsum</p>
      <p class="copy abs white" style="left:23px;top:429px;width:220px">Lorem ipsum dolor sit amet, consectetur adipiscing elit, sed do eiusmod tempor incididunt ut labore et dolore magna aliqua. Ut enim ad minim veniam, quis nostrud exercitation ullamco laboris nisi ut aliquip ex ea commodo consequat.</p>
      <p class="copy abs white" style="left:23px;top:517px;width:220px">Lorem ipsum dolor sit amet, consectetur adipiscing elit, sed do eiusmod tempor incididunt ut labore et dolore magna aliqua. Ut enim ad minim veniam, quis nostrud exercitation ullamco laboris nisi ut aliquip ex ea commodo consequat.</p>
    </div>

    <div class="panel" style="left:268px;width:265px">
      <div class="photo" role="img" aria-label="Photo of therapists playing with a child using a yellow ball" style="left:0;top:0;width:265px;height:130px;background:linear-gradient(120deg,#d7e4ee,#e8c9d6 40%,#f2e04a 60%,#c4d3e4)"></div>
      <svg class="abs" style="left:0;top:80px" width="265" height="60" viewBox="0 0 265 60">
        <path d="M0 55C90 30 180 12 265 30V60H0Z" fill="var(--green)"/>
        <path d="M0 60C90 36 180 22 265 40V60Z" fill="#fff"/>
      </svg>
      <h2 class="title abs" style="left:38px;top:148px;color:var(--orange)">WHY CHOOSE US</h2>
      <p class="sub abs" style="left:0;top:173px;width:265px;text-align:center">What We Do For You</p>

      <div class="tile g" style="left:15px;top:201px"><svg width="46" height="38" viewBox="0 0 46 38" fill="none" stroke="#fff" stroke-width="2.5"><path d="M23 8C16 3 8 3 3 5V33C8 31 16 31 23 36C30 31 38 31 43 33V5C38 3 30 3 23 8Z"/><path d="M23 8V36"/></svg>Lorem ipsum<br>Dolor Sit</div>
      <div class="tile s" style="left:98px;top:201px"><svg width="46" height="38" viewBox="0 0 46 38" fill="#fff"><path d="M23 3L4 18H9V35H37V18H42Z"/><rect x="19" y="24" width="8" height="11" fill="var(--sky)"/></svg>Lorem ipsum<br>Dolor Sit</div>
      <div class="tile g" style="left:178px;top:201px"><svg width="46" height="38" viewBox="0 0 46 38" fill="#fff"><circle cx="14" cy="9" r="6"/><rect x="8" y="17" width="12" height="19" rx="4"/><circle cx="32" cy="9" r="6"/><path d="M26 17H38L41 30H23Z"/></svg>Lorem ipsum<br>Dolor Sit</div>
      <div class="tile s" style="left:15px;top:282px"><svg width="46" height="38" viewBox="0 0 46 38" fill="#fff"><circle cx="23" cy="11" r="8"/><path d="M8 36C8 25 15 21 23 21S38 25 38 36Z"/></svg>Lorem ipsum<br>Dolor Sit</div>
      <div class="tile g" style="left:98px;top:282px"><svg width="46" height="38" viewBox="0 0 46 38" fill="none" stroke="#fff" stroke-width="2.5"><path d="M17 31C5 22 4 14 9 10S18 10 17 14C16 10 22 6 26 10S27 22 17 31Z"/><path d="M30 24C38 18 42 12 38 8S31 8 30 11C29 8 24 7 22 10"/></svg>Lorem ipsum<br>Dolor Sit</div>
      <div class="tile s" style="left:178px;top:282px"><svg width="46" height="38" viewBox="0 0 46 38" fill="#fff"><path d="M16 6L19 14H27L21 19L23 27L16 22L9 27L11 19L5 14H13Z"/><circle cx="33" cy="24" r="8"/></svg>Lorem ipsum<br>Dolor Sit</div>

      <h3 class="abs" style="left:32px;top:408px;font-size:18px;font-weight:600;color:var(--orange)">USER TESTIMONIAL</h3>
      <span class="abs" style="left:30px;top:438px;font-size:30px;font-weight:800;color:var(--orange);line-height:1">“</span>
      <p class="copy abs" style="left:32px;top:461px;width:210px">Lorem ipsum dolor sit amet, consectetur adipiscing elit, sed do eiusmod tempor incididunt ut labore et dolore magna aliqua. Ut enim ad minim veniam, quis nostrud exercitation ullamco laboris nisi ut aliquip ex ea commodo consequat.</p>
      <span class="abs" style="left:226px;top:526px;font-size:30px;font-weight:800;color:var(--orange);line-height:1">”</span>
      <p class="abs" style="left:32px;top:551px;font-size:10px;line-height:12px"><strong style="color:#2aa3dc;font-weight:600">XYZ Name</strong><br>Company Name<br>Country</p>
    </div>

    <div class="panel" style="left:533px;width:267px;background:var(--green)">
      <div class="photo" role="img" aria-label="Faint photo of children playing behind the green panel" style="inset:0;background:radial-gradient(circle at 50% 70%,rgba(90,150,30,.35),transparent 60%)"></div>
      <h2 class="title abs white" style="left:24px;top:23px">KEY TO SUCESS</h2>
      <p class="sub abs white" style="left:24px;top:49px">What Makes Us Successful</p>
      <p class="copy abs white" style="left:24px;top:78px;width:215px">Ut enim ad minim veniam, quis nostrud exercitation ullamco laboris nisi ut aliquip ex ea commodo consequat.</p>
      <p class="copy abs white" style="left:24px;top:132px;font-weight:600">Lorem Ipsum</p>
      <p class="copy abs white" style="left:24px;top:148px;width:215px">Lorem ipsum dolor sit amet, consectetur adipiscing elit, sed do eiusmod tempor incididunt ut labore et dolore magna aliqua. Ut enim ad minim veniam, quis nostrud exercitation ullamco laboris nisi ut aliquip ex ea commodo consequat.</p>

      <div class="feature" style="top:246px"><span class="ico"></span><h4>CONSITENCY</h4><p>Lorem ipsum dolor sit amet, consectetur adipiscing elit, sed do eiusmod tempor incididunt ut labore et dolore magna aliqua.</p></div>
      <div class="feature" style="top:327px"><span class="ico"></span><h4>ACCURACY</h4><p>Lorem ipsum dolor sit amet, consectetur adipiscing elit, sed do eiusmod tempor incididunt ut labore et dolore magna aliqua.</p></div>
      <div class="feature" style="top:408px"><span class="ico"></span><h4>QUALITY</h4><p>Lorem ipsum dolor sit amet, consectetur adipiscing elit, sed do eiusmod tempor incididunt ut labore et dolore magna aliqua.</p></div>

      <p class="copy abs white" style="left:24px;top:503px;width:225px;font-weight:700">Lorem ipsum dolor sit amet, consectetur adipiscing elit, sed do eiusmod tempor incididunt ut labore et dolore magna.</p>
      <p class="copy abs white" style="left:24px;top:556px;width:215px">Ut enim ad minim veniam, quis nostrud exercitation ullamco laboris nisi ut aliquip ex ea commodo consequat.</p>
    </div>
  </section>
</div>
</body>
</html>
```